Now Open Poster

We need a banner for our sports supplement and nutritional store, Harbor Nutrition.
We were hoping for some sort of creative word art piece.
I have drawn my own mock up just to give you all a very basic starting point. But you are free to go with whatever you feel will work best.
The primary objective is simply to explain a little about what the company does, and then direct traffic towards the store with an 'Open Arrow' pointing left.
Text words we have chosen are:
Protein
Creatine
Health
Fitness
Sports Science
Nutrition
Energy
Achievement
Amino Acids
Organic
Supplements
Performance
Testosterone Support
Vitamins
Growth
Diet
Happiness
Weight Loss
Strong
Natural
Vitality
Accomplished
Below the word art we want our logo (See attached options)
Then below the logo the phrase "Success Starts Here"
Dimensions of the poster are 140cm x 60cm.
Colours: Blues/Whites/Greys/Blacks (Lots of white space please)
Here are some cool pieces I found that had some interesting elements that I liked (I'd love to see a mash-up of styles with a street art feel to it. Something funky!):
http://www.moodwall-example.com/pin/100000000000000001/
http://www.moodwall-example.com/pin/100000000000000002/
http://www.moodwall-example.com/pin/100000000000000003/
http://www.moodwall-example.com/pin/100000000000000004/
http://www.moodwall-example.com/pin/100000000000000005/
Thanks for reading, message me if you have any further questions!
- Tobias

```html
<!DOCTYPE html>
<html lang="en">
<head>
<meta charset="utf-8">
<title>Harbor Nutrition – Now Open Banner</title>
<link href="https://fonts.googleapis.com/css2?family=Bebas+Neue&family=Oswald:wght@700&display=swap" rel="stylesheet">
<style>
  :root {
    --stage: #000000;
    --blue-deep: #2f6fd6;
    --blue-mid: #4c8ff0;
    --blue-light: #8cc0ff;
    --ink: #050a14;
    --paper: #ffffff;
    --edge: #cfe3ff;
  }
  * { margin: 0; padding: 0; box-sizing: border-box; }
  html, body { width: 1200px; height: 1000px; overflow: hidden; background: var(--stage); }
  .canvas { position: relative; width: 1200px; height: 1000px; }

  .banner {
    position: absolute; top: 10px; width: 420px; height: 980px;
    border: 1px solid var(--edge); overflow: hidden;
    font-family: "Bebas Neue", "Oswald", sans-serif;
  }
  .banner--slogans { left: 150px; }
  .banner--plain { left: 630px; }

  .banner__backdrop {
    position: absolute; inset: 0;
    background:
      linear-gradient(125deg, transparent 0 30%, rgba(255,255,255,.14) 30% 32%, transparent 32% 60%, rgba(255,255,255,.12) 60% 62%, transparent 62%),
      linear-gradient(160deg, var(--blue-light) 0%, var(--blue-mid) 35%, var(--blue-deep) 70%, var(--blue-mid) 100%);
  }

  .band { position: absolute; left: 0; right: 0; display: flex; align-items: center; justify-content: center; gap: 18px; }
  .band--top { top: 0; height: 60px; border-bottom: 1px solid var(--edge); }
  .band--bottom { bottom: 0; height: 62px; border-top: 1px solid var(--edge); }
  .band__label { color: var(--paper); font-size: 34px; letter-spacing: 1px; line-height: 1; padding-top: 4px; }
  .band--bottom .band__label { font-size: 30px; }

  .wordlist {
    position: absolute; top: 72px; left: 0; right: 0;
    list-style: none; text-align: center;
    font-size: 31px; line-height: 32.6px; letter-spacing: .2px;
  }
  .wordlist li:nth-child(odd) { color: var(--ink); }
  .wordlist li:nth-child(even) { color: var(--paper); }

  .slogan {
    position: absolute; font-family: "Oswald", sans-serif; font-weight: 700;
    color: var(--ink); font-size: 46px; letter-spacing: 2px; white-space: nowrap;
    transform: translate(-50%, -50%) rotate(-90deg);
  }
  .slogan--strong { left: 46px; top: 470px; }
  .slogan--king { left: 376px; top: 470px; }

  .slashes { position: absolute; inset: 0; pointer-events: none; }

  .brand {
    position: absolute; left: 163px; top: 798px; width: 94px; height: 94px;
    border: 1.5px solid var(--ink); border-radius: 50%;
    display: flex; align-items: center; justify-content: center; text-align: center;
    color: var(--ink); font-size: 17px; line-height: 17px;
  }
</style>
</head>
<body>
<div class="canvas">

  <section class="banner banner--slogans">
    <div class="banner__backdrop" role="img" aria-label="Photographic background of folded blue paper with angled light creases"></div>

    <header class="band band--top">
      <svg width="82" height="20" viewBox="0 0 82 20" aria-hidden="true"><g fill="none" stroke="#050a14" stroke-width="2.6"><polyline points="8,2 2,10 8,18"/><polyline points="17,2 11,10 17,18"/><polyline points="26,2 20,10 26,18"/><polyline points="35,2 29,10 35,18"/><polyline points="44,2 38,10 44,18"/><polyline points="53,2 47,10 53,18"/><polyline points="62,2 56,10 62,18"/><polyline points="71,2 65,10 71,18"/><polyline points="80,2 74,10 80,18"/></g></svg>
      <span class="band__label">Open</span>
      <svg width="82" height="20" viewBox="0 0 82 20" aria-hidden="true"><g fill="none" stroke="#050a14" stroke-width="2.6"><polyline points="8,2 2,10 8,18"/><polyline points="17,2 11,10 17,18"/><polyline points="26,2 20,10 26,18"/><polyline points="35,2 29,10 35,18"/><polyline points="44,2 38,10 44,18"/><polyline points="53,2 47,10 53,18"/><polyline points="62,2 56,10 62,18"/><polyline points="71,2 65,10 71,18"/><polyline points="80,2 74,10 80,18"/></g></svg>
    </header>

    <svg class="slashes" width="420" height="980" viewBox="0 0 420 980" aria-hidden="true">
      <g fill="#ffffff">
        <polygon points="18,120 72,102 72,110 18,128"/>
        <polygon points="18,144 72,126 72,134 18,152"/>
        <polygon points="18,168 72,150 72,158 18,176"/>
        <polygon points="18,192 72,174 72,182 18,200"/>
        <polygon points="18,216 72,198 72,206 18,224"/>
        <polygon points="18,240 72,222 72,230 18,248"/>

        <polygon points="18,690 72,672 72,680 18,698"/>
        <polygon points="18,714 72,696 72,704 18,722"/>
        <polygon points="18,738 72,720 72,728 18,746"/>
        <polygon points="18,762 72,744 72,752 18,770"/>
        <polygon points="18,786 72,768 72,776 18,794"/>

        <polygon points="348,155 402,137 402,145 348,163"/>
        <polygon points="348,179 402,161 402,169 348,187"/>
        <polygon points="348,203 402,185 402,193 348,211"/>
        <polygon points="348,227 402,209 402,217 348,235"/>
        <polygon points="348,251 402,233 402,241 348,259"/>

        <polygon points="348,655 402,637 402,645 348,663"/>
        <polygon points="348,679 402,661 402,669 348,687"/>
        <polygon points="348,703 402,685 402,693 348,711"/>
        <polygon points="348,727 402,709 402,717 348,735"/>
        <polygon points="348,751 402,733 402,741 348,759"/>
        <polygon points="348,775 402,757 402,765 348,783"/>
      </g>
    </svg>

    <p class="slogan slogan--strong">I AM STRONG</p>
    <p class="slogan slogan--king">I AM KING</p>

    <ul class="wordlist">
      <li>Protein</li><li>Creatine</li><li>Health</li><li>Fitness</li><li>Sports Science</li><li>Nutrition</li><li>Energy</li><li>Achievement</li><li>Amino Acids</li><li>Organic</li><li>Supplements</li><li>Performance</li><li>Testosterone Support</li><li>Vitamins</li><li>Growth</li><li>Diet</li><li>Happiness</li><li>Weight Loss</li><li>Strong</li><li>Natural</li><li>Vitality</li><li>Accomplished</li>
    </ul>

    <div class="brand">Harbor<br>Nutrition</div>

    <footer class="band band--bottom">
      <svg width="56" height="22" viewBox="0 0 56 22" aria-hidden="true"><g stroke="#050a14" stroke-width="3.4"><line x1="2" y1="21" x2="10" y2="1"/><line x1="13" y1="21" x2="21" y2="1"/><line x1="24" y1="21" x2="32" y2="1"/><line x1="35" y1="21" x2="43" y2="1"/><line x1="46" y1="21" x2="54" y2="1"/></g></svg>
      <span class="band__label">Success Starts Here</span>
      <svg width="56" height="22" viewBox="0 0 56 22" aria-hidden="true"><g stroke="#050a14" stroke-width="3.4"><line x1="2" y1="21" x2="10" y2="1"/><line x1="13" y1="21" x2="21" y2="1"/><line x1="24" y1="21" x2="32" y2="1"/><line x1="35" y1="21" x2="43" y2="1"/><line x1="46" y1="21" x2="54" y2="1"/></g></svg>
    </footer>
  </section>

  <section class="banner banner--plain">
    <div class="banner__backdrop" role="img" aria-label="Photographic background of folded blue paper with angled light creases"></div>

    <header class="band band--top">
      <svg width="82" height="20" viewBox="0 0 82 20" aria-hidden="true"><g fill="none" stroke="#050a14" stroke-width="2.6"><polyline points="8,2 2,10 8,18"/><polyline points="17,2 11,10 17,18"/><polyline points="26,2 20,10 26,18"/><polyline points="35,2 29,10 35,18"/><polyline points="44,2 38,10 44,18"/><polyline points="53,2 47,10 53,18"/><polyline points="62,2 56,10 62,18"/><polyline points="71,2 65,10 71,18"/><polyline points="80,2 74,10 80,18"/></g></svg>
      <span class="band__label">Open</span>
      <svg width="82" height="20" viewBox="0 0 82 20" aria-hidden="true"><g fill="none" stroke="#050a14" stroke-width="2.6"><polyline points="8,2 2,10 8,18"/><polyline points="17,2 11,10 17,18"/><polyline points="26,2 20,10 26,18"/><polyline points="35,2 29,10 35,18"/><polyline points="44,2 38,10 44,18"/><polyline points="53,2 47,10 53,18"/><polyline points="62,2 56,10 62,18"/><polyline points="71,2 65,10 71,18"/><polyline points="80,2 74,10 80,18"/></g></svg>
    </header>

    <ul class="wordlist">
      <li>Protein</li><li>Creatine</li><li>Health</li><li>Fitness</li><li>Sports Science</li><li>Nutrition</li><li>Energy</li><li>Achievement</li><li>Amino Acids</li><li>Organic</li><li>Supplements</li><li>Performance</li><li>Testosterone Support</li><li>Vitamins</li><li>Growth</li><li>Diet</li><li>Happiness</li><li>Weight Loss</li><li>Strong</li><li>Natural</li><li>Vitality</li><li>Accomplished</li>
    </ul>

    <div class="brand">Harbor<br>Nutrition</div>

    <footer class="band band--bottom">
      <svg width="56" height="22" viewBox="0 0 56 22" aria-hidden="true"><g stroke="#050a14" stroke-width="3.4"><line x1="2" y1="21" x2="10" y2="1"/><line x1="13" y1="21" x2="21" y2="1"/><line x1="24" y1="21" x2="32" y2="1"/><line x1="35" y1="21" x2="43" y2="1"/><line x1="46" y1="21" x2="54" y2="1"/></g></svg>
      <span class="band__label">Success Starts Here</span>
      <svg width="56" height="22" viewBox="0 0 56 22" aria-hidden="true"><g stroke="#050a14" stroke-width="3.4"><line x1="2" y1="21" x2="10" y2="1"/><line x1="13" y1="21" x2="21" y2="1"/><line x1="24" y1="21" x2="32" y2="1"/><line x1="35" y1="21" x2="43" y2="1"/><line x1="46" y1="21" x2="54" y2="1"/></g></svg>
    </footer>
  </section>

</div>
</body>
</html>
```